UK vitamin company needs a packaging label design for new vitamin range

We have a logo, and we have the product. We now need some beautiful labels to go on the boxes which bring the product range to life.
We have 7 categories: Joint Care, Heart Heath, Brain Function, Immune System, Skin, Antioxidants and Probiotics. Each of these categories should have its own look within the plumble tonic range. This can be quite subtle, but needs to be clearly visible and should be linked to the category e.g. 'Heart Health' might have a heart etc.
I have uploaded the logo, an example of the pack shape, and the sizing info for the label.
We are a fun brand, so please have some fun with this. We want the labels to be bold, and differentiated from the rest of the category.
Thanks
All images used must be 'rights free'. Many thanks
UK
It Company

```html
<!DOCTYPE html>
<html lang="en">
<head>
<meta charset="utf-8">
<title>plumble tonic – Antioxidants label</title>
<link rel="stylesheet" href="https://fonts.googleapis.com/css2?family=Oswald:wght@400;500;700&display=swap">
<style>
  :root {
    --page: #f4f4f4;
    --label: #ffffff;
    --brand-blue: #1a4fa8;
    --brand-orange: #ee7a1c;
    --ink-white: #ffffff;
    --ink-soft: #dfe7f5;
  }
  html, body {
    margin: 0;
    padding: 0;
    width: 1200px;
    height: 1194px;
    overflow: hidden;
    background: var(--page);
  }
  .canvas {
    position: relative;
    width: 1200px;
    height: 1194px;
  }
  .label {
    position: absolute;
    left: 250px;
    top: 75px;
    width: 700px;
    height: 1044px;
    background: var(--label);
    box-shadow: 0 2px 10px rgba(0,0,0,0.08);
    font-family: "Oswald", sans-serif;
  }
  .label__top-rule {
    position: absolute;
    left: 0; right: 0; top: 16px;
    height: 10px;
    background: var(--brand-blue);
  }
  .label__bottom-band {
    position: absolute;
    left: 0; right: 0; bottom: 40px;
    height: 48px;
    background: var(--brand-blue);
  }
  .brand-name {
    position: absolute;
    top: 150px;
    left: 0; right: 0;
    text-align: center;
    font-weight: 500;
    font-size: 64px;
    line-height: 1;
    letter-spacing: 1px;
    color: var(--brand-orange);
  }
  .category-badge {
    position: absolute;
    left: 95px;
    top: 345px;
    width: 510px;
    height: 510px;
  }
  .badge-text {
    position: absolute;
    inset: 0;
    color: var(--ink-white);
    text-align: center;
  }
  .badge-text__range {
    position: absolute;
    top: 150px; left: 0; right: 0;
    font-size: 17px;
    line-height: 1;
    letter-spacing: 2px;
    color: var(--ink-soft);
  }
  .badge-text__category {
    position: absolute;
    top: 196px; left: 0; right: 0;
    font-weight: 700;
    font-size: 66px;
    line-height: 1.2;
    letter-spacing: 1px;
  }
  .badge-text__blurb {
    position: absolute;
    top: 300px; left: 110px; right: 110px;
    font-size: 14px;
    line-height: 1.35;
    letter-spacing: 0.5px;
    color: var(--ink-soft);
  }
  .badge-text__count {
    position: absolute;
    top: 386px; left: 0; right: 0;
    font-weight: 700;
    font-size: 26px;
    line-height: 1.2;
    letter-spacing: 1px;
  }
  .badge-text__count small {
    font-size: 15px;
    letter-spacing: 1px;
  }
</style>
</head>
<body>
<main class="canvas">
  <section class="label">
    <div class="label__top-rule"></div>

    <div class="brand-name">plumble tonic</div>

    <div class="category-badge">
      <svg width="510" height="510" viewBox="0 0 510 510" aria-hidden="true">
        <defs>
          <path id="badge-arc" d="M 70 255 A 185 185 0 0 1 440 255"/>
        </defs>
        <circle cx="255" cy="255" r="250" fill="var(--brand-blue)"/>
        <circle cx="255" cy="255" r="222" fill="none" stroke="var(--ink-white)" stroke-width="5"/>
        <text font-family="Oswald, sans-serif" font-weight="700" font-size="20" letter-spacing="3" fill="var(--ink-white)">
          <textPath href="#badge-arc" startOffset="50%" text-anchor="middle">• NATURAL ELEMENTS •</textPath>
        </text>
        <line x1="80" y1="285" x2="430" y2="285" stroke="var(--ink-white)" stroke-width="3"/>
        <line x1="120" y1="372" x2="390" y2="372" stroke="var(--ink-white)" stroke-width="2"/>
      </svg>
      <div class="badge-text">
        <div class="badge-text__range">- B1 • B2 • B7 -</div>
        <div class="badge-text__category">ANTIOXIDANTS</div>
        <div class="badge-text__blurb">PURE DAILY SUPPORT FORMULA<br>WITH CAREFULLY CHOSEN NUTRIENTS<br>FOR ENERGY AND WELLBEING</div>
        <div class="badge-text__count">60 <small>SOFTGELS</small></div>
      </div>
    </div>

    <div class="label__bottom-band"></div>
  </section>
</main>
</body>
</html>
```